Maplebrook Self Storage - Business Sign

The sign we are needing designed is our main road sign for our self-storage business. The dimensions of the sign are 57 inches tall x 96 inches wide. We require that our attached logo be on the sign as well as our phone number: 478-216-7745 and website www.MaplebrookStorage.net. Optional information that can be added but not required is our address: 418 Delmont Ridge Pkwy, Centerville, GA 31044.

Industry/Entity Type

Self Storage

Font styles to use
Sans Serif

```html
<!DOCTYPE html>
<html lang="en">
<head>
<meta charset="utf-8">
<title>Maplebrook Self Storage – Road Sign</title>
<link href="https://fonts.googleapis.com/css2?family=Barlow+Condensed:wght@500;600&family=Barlow:wght@600&family=Dancing+Script:wght@700&display=swap" rel="stylesheet">
<style>
  :root {
    --page-bg: #eef0f2;
    --sign-bg: #ffffff;
    --ink-dark: #2f2f31;
    --ink-gray: #6b6b6e;
    --brand-blue: #1257b0;
    --accent-blue: #2f7fd0;
    --band-edge: #c9ccd1;
    --on-blue: #ffffff;
  }
  * { margin: 0; padding: 0; box-sizing: border-box; }
  html, body {
    width: 1063px;
    height: 1200px;
    overflow: hidden;
    background: var(--page-bg);
  }
  .canvas {
    width: 1063px;
    height: 1200px;
    display: flex;
    align-items: center;
    justify-content: center;
  }
  .road-sign {
    position: relative;
    width: 1000px;
    height: 594px;
    background: var(--sign-bg);
    box-shadow: 0 6px 18px rgba(0,0,0,0.25);
    display: flex;
    flex-direction: column;
  }
  .tagline {
    margin-top: 28px;
    text-align: center;
    font-family: "Barlow Condensed", sans-serif;
    font-weight: 500;
    font-size: 42px;
    color: var(--ink-dark);
    letter-spacing: 0.2px;
  }
  .tagline .tagline-accent {
    font-family: "Dancing Script", cursive;
    font-weight: 700;
    font-size: 44px;
    color: var(--accent-blue);
  }
  .brand-name {
    flex: 1;
    display: flex;
    flex-direction: column;
    align-items: center;
    justify-content: center;
    font-family: "Barlow", sans-serif;
    font-weight: 600;
    color: var(--ink-dark);
    line-height: 1;
    padding-bottom: 10px;
  }
  .brand-name .brand-primary {
    font-size: 150px;
    letter-spacing: -1px;
  }
  .brand-name .brand-secondary {
    margin-top: 18px;
    font-size: 72px;
    letter-spacing: 14px;
  }
  .contact-band {
    height: 92px;
    background: var(--brand-blue);
    border-top: 6px solid var(--band-edge);
    display: flex;
    align-items: center;
    justify-content: center;
    gap: 16px;
    font-family: "Barlow Condensed", sans-serif;
    font-weight: 600;
    font-size: 50px;
    color: var(--on-blue);
  }
  .contact-item {
    display: flex;
    align-items: center;
    gap: 10px;
  }
  .contact-icon {
    width: 34px;
    height: 34px;
    flex: none;
  }
</style>
</head>
<body>
<main class="canvas">
  <section class="road-sign" aria-label="Maplebrook Self Storage road sign">
    <p class="tagline">Find your <span class="tagline-accent">Secure</span> Self Storage Solution in No Time!</p>

    <h1 class="brand-name">
      <span class="brand-primary">Maplebrook</span>
      <span class="brand-secondary">SELF STORAGE</span>
    </h1>

    <footer class="contact-band">
      <span class="contact-item">
        <svg class="contact-icon" viewBox="0 0 24 24" aria-hidden="true">
          <path fill="#ffffff" d="M6.6 10.8a15.1 15.1 0 0 0 6.6 6.6l2.2-2.2a1 1 0 0 1 1-.25 11.4 11.4 0 0 0 3.6.57 1 1 0 0 1 1 1V20a1 1 0 0 1-1 1A17 17 0 0 1 3 4a1 1 0 0 1 1-1h3.5a1 1 0 0 1 1 1c0 1.25.2 2.45.57 3.57a1 1 0 0 1-.25 1z"/>
          <path fill="none" stroke="#ffffff" stroke-width="1.6" stroke-linecap="round" d="M14.5 3.5a6 6 0 0 1 6 6M14.5 7a2.6 2.6 0 0 1 2.6 2.6"/>
        </svg>
        <span class="contact-phone">478-216-7745</span>
      </span>
      <span class="contact-item">
        <svg class="contact-icon" viewBox="0 0 24 24" aria-hidden="true">
          <g fill="none" stroke="#ffffff" stroke-width="1.6">
            <circle cx="12" cy="12" r="9.5"/>
            <ellipse cx="12" cy="12" rx="4.2" ry="9.5"/>
            <path d="M2.5 12h19M4 7h16M4 17h16"/>
          </g>
        </svg>
        <span class="contact-web">MaplebrookStorage.net</span>
      </span>
    </footer>
  </section>
</main>
</body>
</html>
```